Business Card Design Project - Harbourline Removals

I need a business card design created for my furniture removal business. The name is Harbourline Removals so something associated with the galaxy would be great ( possibly the southern cross or something to that effect). Modern, creative and simple was what I had in mind. I like metallic silver and different shades of blue but am open to other colour ideas.

Industry/Entity Type

Business

Requirements
Must have
• Something associated with the galaxy
Nice to have
• Have checked out lots of different fontstyles and really like 'kefa'

```html
<!DOCTYPE html>
<html lang="en">
<head>
<meta charset="utf-8">
<title>Harbourline Removals – Business Card</title>
<link rel="stylesheet" href="https://fonts.googleapis.com/css2?family=Niconne&family=Tinos&display=swap">
<style>
  :root {
    --card-bg: #ffffff;
    --orb-blue: #3838e6;
    --star-white: #ffffff;
    --title-white: #ffffff;
    --title-shadow: rgba(0, 0, 20, 0.85);
    --contact-ink: #1a1a1a;
  }
  html, body {
    margin: 0;
    padding: 0;
    overflow: hidden;
    background: var(--card-bg);
  }
  .business-card {
    position: relative;
    width: 1200px;
    height: 686px;
    background: var(--card-bg);
    overflow: hidden;
  }
  .orb {
    position: absolute;
    inset: 0;
    width: 1200px;
    height: 686px;
  }
  .orb-shape {
    fill: var(--orb-blue);
  }
  .southern-cross circle {
    fill: var(--star-white);
  }
  .company-name {
    position: absolute;
    top: 22px;
    right: 22px;
    margin: 0;
    font-family: "Niconne", cursive;
    font-weight: 400;
    font-style: normal;
    font-size: 78px;
    line-height: 1.1;
    color: var(--title-white);
    text-shadow: 6px 7px 6px var(--title-shadow);
    white-space: nowrap;
  }
  .contact {
    position: absolute;
    left: 23px;
    bottom: 14px;
    margin: 0;
    font-family: "Tinos", "Times New Roman", serif;
    font-style: normal;
    font-size: 33px;
    line-height: 46px;
    color: var(--contact-ink);
  }
  .contact p {
    margin: 0;
  }
</style>
</head>
<body>
  <main class="business-card">
    <svg class="orb" viewBox="0 0 1200 686" role="img" aria-label="Blue orb with the stars of the Southern Cross">
      <ellipse class="orb-shape" cx="820" cy="272" rx="385" ry="345"/>
      <g class="southern-cross">
        <circle cx="830" cy="215" r="7"/>
        <circle cx="842" cy="470" r="8"/>
        <circle cx="748" cy="335" r="6"/>
        <circle cx="935" cy="310" r="6.5"/>
        <circle cx="872" cy="385" r="4"/>
      </g>
    </svg>
    <h1 class="company-name">Harbourline Removals</h1>
    <address class="contact">
      <p class="contact-phone">Contact# 0412 555 017</p>
      <p class="contact-web">WWW.Harbourlineremovals.com.au</p>
    </address>
  </main>
</body>
</html>
```